Elegant, High End Integrated Wellness Healthcare Practice

We need a brochure designed for an integrated mind-body wellness healthcare practice (www.larkfernclinic.com) . This brochure will be used when we cold call prospects (physicians to refer to our office, and potential consumers to utilize our services). Our practice is geographically located in the middle Tennessee USA region, although we have plans to become an international company as many of our offerings can be accessed anywhere in the world. Ultimately our goal is to have this brochure used as a leave-behind in an effort to introduce our integrated offerings to increase market share. The final product brochure should be both elegant and serious, with clean lines but also convey warmth and trust, as individuals who are coming for our services have usually struggled with their health for a significant amount of time before finding our practice.
Updates

The design brief was very specific about providing a high-end science-based 2-page brochure (not flier). Several designs submitted were fliers. The other designs were heavy on yoga or "woo woo" non-science-based looking pictures. This is a flier to appeal to physicians and other healthcare providers. Therefore the design must speak science and evidence-based methods of mind and body wellness care. I would also like to appeal to the other designers I paid extra for their submissions and who have indicated they will "respond in the coming days."

```html
<!DOCTYPE html>
<html lang="en">
<head>
<meta charset="utf-8">
<title>Larkfern Clinic Brochure</title>
<link href="https://fonts.googleapis.com/css2?family=Cinzel:wght@500&family=Poppins:ital,wght@0,400;0,500;0,600;0,700;1,700&display=swap" rel="stylesheet">
<style>
:root{
  --green:#6db33f;
  --green-dark:#4f8f2c;
  --green-light:#c3e0ad;
  --ink:#1f2a1a;
  --ring:#223a1c;
  --paper:#eef4ea;
  --backdrop:#a9a9a9;
  --star:#f37021;
}
*{margin:0;padding:0;box-sizing:border-box}
html,body{width:1200px;height:950px;overflow:hidden;background:var(--backdrop);font-family:'Poppins',sans-serif}
.spread{position:absolute;left:99px;top:88px;width:1001px;height:774px;display:flex;box-shadow:0 6px 18px rgba(0,0,0,.35)}
.panel{position:relative;width:500px;height:774px;overflow:hidden;background:var(--paper)}
.panel--front{width:501px;background:linear-gradient(90deg,#c9cec6 0%,#e6ebe2 12%,var(--paper) 40%)}
.bg{position:absolute;left:0;top:0}
.abs{position:absolute}
.tagline{left:0;width:500px;top:30px;text-align:center;color:#fff;font-style:italic;font-weight:700;font-size:19.5px}
.team-title{left:0;width:500px;top:86px;text-align:center;color:#fff;font-family:'Cinzel',serif;font-weight:500;font-size:20px;line-height:24.5px;text-transform:uppercase}
.rule{left:195px;top:173px;width:110px;height:3px;background:#fff}
.intro{left:25px;width:450px;top:196px;text-align:center;color:#fff;font-size:10.8px;line-height:13.8px}
.member{top:312px;width:132px;height:132px;border-radius:50%;background:var(--ring);display:flex;align-items:center;justify-content:center;box-shadow:0 0 0 4px var(--green-dark)}
.member .photo{width:110px;height:110px;border-radius:50%;background:linear-gradient(160deg,#d8cfc4,#8a7565)}
.name{top:454px;width:160px;text-align:center;color:var(--green);font-weight:700;font-size:12px}
.quote{left:45px;width:410px;text-align:center;color:var(--ink);font-size:10.3px;line-height:13.2px}
.stars{left:0;width:500px}
.initials{left:0;width:500px;text-align:center;color:var(--green);font-weight:600;font-size:11.5px}
.divider{left:45px;top:581px;width:410px;height:1px;background:var(--ink)}
.pill{left:45px;top:688px;width:162px;height:26px;border-radius:8px;background:var(--green);color:#fff;font-size:14px;font-weight:500;text-align:center;line-height:26px}
.phone{left:44px;top:722px;display:flex;align-items:center;gap:10px;font-weight:600;font-size:20px;color:var(--ink)}
.info{left:233px;display:flex;align-items:flex-start;gap:10px;font-size:11px;color:var(--ink);line-height:13px}
.icon{width:26px;height:26px;flex:none}
.brand{left:0;width:501px;top:536px;display:flex;justify-content:center;align-items:center;gap:12px}
.brand-mark{width:54px;height:54px;border-radius:50%;background:var(--green-dark)}
.brand-name{font-weight:600;font-size:22px;color:var(--ink);letter-spacing:1px}
.headline{left:0;width:501px;top:612px;text-align:center;font-weight:700;font-size:34px;line-height:39px;color:var(--ink)}
.headline .accent{color:var(--green)}
.sub{left:0;width:501px;top:702px;text-align:center;font-size:14px;line-height:17px;color:var(--ink)}
.sub strong{font-style:italic;font-weight:700}
</style>
</head>
<body>
<main class="spread">
  <section class="panel panel--back">
    <svg class="bg" width="500" height="774" viewBox="0 0 500 774">
      <path d="M0 0H500V330C450 360 420 410 360 420 250 440 140 430 70 470 30 495 10 520 0 560Z" fill="#bfe0a5"/>
      <path d="M0 0H500V315C440 350 410 400 350 410 250 425 130 415 60 460 25 485 8 510 0 540Z" fill="var(--green)"/>
    </svg>
    <p class="abs tagline">Find A Clearer Path To A Stronger You</p>
    <h2 class="abs team-title">Meet Our Team At<br>Larkfern Clinic<br>In Alder Falls, TN</h2>
    <div class="abs rule"></div>
    <p class="abs intro">Meet the experienced team at Larkfern Clinic, we facilitate body &amp; mind health and wellness through an integrated functional approach to care that is unique to you. For more information, call us or schedule an appointment online. We are conveniently located at 480 Birchwood Ln. Alder Falls, TN 37999. We serve clients in Cedar Hollow, Alder Falls, Westmere, Pine Ridge, Ashcombe, TN, and surrounding areas.</p>

    <div class="abs member" style="left:39px"><div class="photo" role="img" aria-label="Portrait photo of Dr. Nora Hale"></div></div>
    <div class="abs member" style="left:184px"><div class="photo" role="img" aria-label="Portrait photo of Dr. Owen Pratt"></div></div>
    <div class="abs member" style="left:331px"><div class="photo" role="img" aria-label="Portrait photo of Claire Dunmore"></div></div>
    <p class="abs name" style="left:26px">DR. NORA HALE</p>
    <p class="abs name" style="left:170px">DR. OWEN PRATT</p>
    <p class="abs name" style="left:317px">CLAIRE DUNMORE</p>

    <p class="abs quote" style="top:491px">“ Dr. Hale is amazing at giving advice on how to handle different situations. Amazing listener and very good at explaining how to figure out certain behaviors or feelings one may be experiencing. ”</p>
    <svg class="abs stars" style="top:536px" height="16" viewBox="0 0 500 16"><g fill="var(--star)">
      <polygon id="st" points="218,0 220.4,5.3 226,5.8 221.8,9.6 223,15 218,12.2 213,15 214.2,9.6 210,5.8 215.6,5.3"/>
      <use href="#st" x="16"/><use href="#st" x="32"/><use href="#st" x="48"/><use href="#st" x="64"/></g></svg>
    <p class="abs initials" style="top:557px">K.L.</p>
    <div class="abs divider"></div>
    <p class="abs quote" style="top:597px">“ I have not been to therapy in a long while and I really enjoyed the experience. I felt not only heard but also listened to. ”</p>
    <svg class="abs stars" style="top:631px" height="16" viewBox="0 0 500 16"><g fill="var(--star)">
      <use href="#st"/><use href="#st" x="16"/><use href="#st" x="32"/><use href="#st" x="48"/><use href="#st" x="64"/></g></svg>
    <p class="abs initials" style="top:651px">S. T.</p>

    <div class="abs pill">Contact information</div>
    <div class="abs phone">
      <svg class="icon" viewBox="0 0 26 26"><circle cx="13" cy="13" r="13" fill="var(--green)"/><path d="M9 7l2.5 0 1 3-1.5 1.2c.8 1.8 2 3 3.8 3.8L16 13.5l3 1v2.5c0 .6-.5 1-1 1C12 18 8 14 8 8c0-.5.4-1 1-1z" fill="#fff"/></svg>
      <span>55501 23456</span>
    </div>
    <div class="abs info" style="top:689px">
      <svg class="icon" viewBox="0 0 26 26"><circle cx="13" cy="13" r="13" fill="var(--green)"/><g fill="none" stroke="#fff" stroke-width="1.4"><circle cx="13" cy="13" r="7"/><ellipse cx="13" cy="13" rx="3" ry="7"/><path d="M6 13h14M7.5 9.5h11M7.5 16.5h11"/></g></svg>
      <span style="line-height:26px;font-size:11.5px">www.larkfernclinic.com</span>
    </div>
    <div class="abs info" style="top:713px">
      <svg class="icon" viewBox="0 0 26 26"><circle cx="13" cy="13" r="13" fill="var(--green)"/><path d="M13 5a5.5 5.5 0 0 0-5.5 5.5C7.5 15 13 21 13 21s5.5-6 5.5-10.5A5.5 5.5 0 0 0 13 5z" fill="#fff"/><circle cx="13" cy="10.5" r="2.2" fill="var(--green)"/></svg>
      <span>480 Birchwood Ln. Alder Falls,<br>TN 37999</span>
    </div>
  </section>

  <section class="panel panel--front">
    <svg class="bg" width="501" height="774" viewBox="0 0 501 774">
      <circle cx="268" cy="222" r="290" fill="var(--green-light)"/>
      <circle cx="268" cy="200" r="278" fill="var(--green)"/>
      <path d="M0 0H160C80 60 30 150 25 240 20 300 10 330 0 340Z" fill="var(--green-dark)" opacity=".5"/>
    </svg>
    <div class="abs" style="left:36px;top:-2px;width:464px;height:464px;border-radius:50%;background:radial-gradient(circle at 55% 45%,#8a7a5e,#4f5e3c 60%,#3b4a2c)" role="img" aria-label="Photo of a woman outdoors holding a fern leaf to her face"></div>
    <div class="abs brand"><span class="brand-mark"></span><span class="brand-name">LARKFERN CLINIC</span></div>
    <h1 class="abs headline"><span class="accent">Find</span> A Clearer<br>Path To <span class="accent">A Stronger You</span></h1>
    <p class="abs sub">Larkfern Clinic, integrated body and mind<br>health, wellness center located in <strong>ALDER FALLS, TN</strong></p>
  </section>
</main>
</body>
</html>
```